Power point template

I would like to ppt template to use for a research project. The key topic of the research project is: A cyber security toolkit to protect the privacy data/infrastructure of the health care industry.This file will be used by the entire research team (approx. 50 person) to communicate internally during their official meeting but also to present the project results at the Varnholt Assembly, Conferences and so on. Therefore, the design should be professional, and official. The fact that the ppt will be used by several person for the same project means that the template should allow the user any time (s)he adds a table to have a particular format. Any time the user adds bullet points, these should have a particular color and shape.About the ppt design, you should use the project logo that I am attaching and of course you may use at the layout colors that matches to this logo. Regarding its structure I am attaching the basic ppt (non-professional), without design. You may notice at the bottom of each slide there is the VA flag and a particular phrase beside. Please use that in your proposal as well. You may find images for the VA flag here: https://varnholt-assembly.example/about-va/emblems/banner_en If you need any further clarifications, please do not hesitate to contact me.

```html
<!DOCTYPE html>
<html lang="en">
<head>
<meta charset="utf-8">
<title>KESTREL presentation template</title>
<link href="https://fonts.googleapis.com/css2?family=Michroma&family=Lato:wght@400;700&display=swap" rel="stylesheet">
<style>
:root{
  --teal-deep:#169d93;
  --teal:#1caea3;
  --teal-mid:#22bdb1;
  --teal-bright:#2bd3c6;
  --teal-glow:#36e0d3;
  --ink:#7a7a7a;
  --paper:#f5f5f5;
  --foot:#c8c8c8;
  --flag:#1f3f9c;
  --stage:#141414;
}
*{margin:0;padding:0;box-sizing:border-box}
html,body{width:1200px;height:1158px;overflow:hidden;background:var(--stage)}
body{position:relative;font-family:'Lato',sans-serif}
.slide{position:absolute;width:386px;height:275px;background:var(--paper);overflow:hidden}
.slide.teal{background:radial-gradient(circle at 70% 40%,var(--teal-mid),var(--teal) 70%)}
.col1{left:14px}.col2{left:410px}.col3{left:806px}
.row1{top:11px}.row2{top:296px}.row3{top:579px}.row4{top:871px}

.head{position:absolute;left:0;top:9px;height:20px;border-left:4px solid var(--teal);padding-left:6px;
  font-family:'Michroma',sans-serif;font-size:13.5px;line-height:20px;color:var(--teal);letter-spacing:.3px}
.brand{position:absolute;right:9px;top:8px;display:flex;align-items:center;gap:3px;
  font-size:12px;color:var(--teal);letter-spacing:.5px}
.brand .dot{width:14px;height:14px;border:2px solid currentColor;border-radius:50%}

.foot{position:absolute;left:0;right:0;bottom:0;height:20px;background:var(--foot);display:flex;align-items:center}
.teal .foot{background:var(--teal-deep)}
.flag{width:25px;height:16px;margin:0 6px 0 3px;background:var(--flag);flex:none}
.foot p{font-size:4.4px;line-height:1.5;color:#555;padding-right:10px}
.teal .foot p{color:#fff}

.copy{font-size:5.6px;line-height:1.72;color:var(--ink);text-align:justify}
.copy.center{text-align:center}
.copy.white{color:#fff}
.ptitle{display:flex;align-items:center;gap:4px;font-size:7.5px;font-weight:700;color:var(--teal);margin-bottom:3px;text-transform:uppercase}
.ptitle .ring{width:9px;height:9px;border:1.5px solid var(--teal);border-radius:50%;flex:none}
.media{position:absolute;background:linear-gradient(135deg,#0e6f79,#1fb3b0 55%,#47d6d0)}

.hero-brand{position:absolute;right:26px;top:70px;display:flex;align-items:center;gap:6px;color:#fff;font-size:33px;letter-spacing:1.5px}
.hero-brand .dot{width:40px;height:40px;border:4px solid #fff;border-radius:50%}
.hero-tag{position:absolute;right:26px;top:114px;text-align:right;color:#fff;font-size:8.4px;line-height:1.3}
.hero-title{position:absolute;right:26px;top:156px;font-family:'Michroma',sans-serif;font-weight:400;color:#fff;font-size:18px}
.hero-meta{position:absolute;right:26px;top:187px;text-align:right;color:#fff;font-size:8.8px;line-height:1.6}
.hero-meta b{font-weight:700}

.cover-brand{position:absolute;left:0;right:0;top:84px;display:flex;justify-content:center;align-items:center;gap:6px;color:#fff;font-size:27px;letter-spacing:1.5px}
.cover-brand .dot{width:33px;height:33px;border:3.5px solid #fff;border-radius:50%}
.cover-title{position:absolute;left:0;right:0;top:143px;text-align:center;font-family:'Michroma',sans-serif;font-weight:400;font-size:19px;color:#fff}
.cover-sub{position:absolute;left:0;right:0;top:172px;text-align:center;color:#fff;font-size:11.5px;font-weight:700;letter-spacing:.4px}

.member{position:absolute;top:72px;width:106px;text-align:center}
.member .portrait{width:60px;height:60px;margin:0 auto 6px;border-radius:50%;background:linear-gradient(#e4e4e4,#9a9a9a);border:1px solid #ddd}
.member h3{font-size:8.6px;font-weight:400;color:var(--teal);letter-spacing:.3px}
.member h4{font-size:5.8px;font-weight:400;color:#555;margin:1px 0 3px}
.member .copy{font-size:5.8px}

.features{position:absolute;left:0;top:50px;width:386px;height:184px;display:flex}
.feature{flex:1;padding:14px 9px 0;text-align:center}
.feature svg{display:block;margin:0 auto 12px}
.f1{background:var(--teal-deep)}.f2{background:var(--teal)}.f3{background:var(--teal-mid)}.f4{background:var(--teal-glow)}

.band{position:absolute;left:0;width:386px;background:var(--teal)}
.thumb{position:absolute;top:57px;width:99px;height:61px}
.thumb-text{position:absolute;top:125px;width:99px}
.thumb-text h3{font-size:9.4px;font-weight:700;color:#fff;margin-bottom:1px}
.label{position:absolute;left:0;top:41px;background:var(--teal);color:#fff;font-size:11.5px;font-weight:700;padding:3px 4px;letter-spacing:.3px}
.kick-title{font-size:11.5px;font-weight:700;color:#fff;margin-bottom:4px}

.bullet{position:absolute;left:15px;width:358px}

.grid{position:absolute;left:12px;top:96px;width:364px;border-collapse:separate;border-spacing:0 2px}
.grid th{background:var(--teal);color:#fff;font-size:7.2px;text-align:left;padding:4px 8px;height:18px}
.grid td{font-size:5px;line-height:1.5;color:#666;padding:2px 8px;height:23px;background:#fafafa}
.grid td.key{width:70px;color:var(--teal);font-size:6.3px;text-align:center;background:#e9e9e9}
</style>
</head>
<body>

<section class="slide teal col1 row1">
  <div class="hero-brand"><span class="dot"></span>KESTREL</div>
  <p class="hero-tag">An Integrated Data Protection<br>Suite for Clinical Networks</p>
  <h1 class="hero-title">Presentation Title</h1>
  <p class="hero-meta"><b>Meeting title:</b> Title Here<br><b>Presenter name:</b> Name Here<br><b>Presenter organisation:</b> Organisation Name<br><b>Date:</b> 07-02-2019</p>
  <footer class="foot"><span class="flag"></span><p>This project has received funding from the Varnholt Assembly's Meridian 2020 research and innovation programme under grant agreement No 904417 Connected Services, Digital Trust &amp; Care Systems Resilience</p></footer>
</section>

<section class="slide teal col2 row1">
  <div class="cover-brand"><span class="dot"></span>KESTREL</div>
  <h2 class="cover-title">SECTION TITLE HERE</h2>
  <p class="cover-sub">Subtext here</p>
  <footer class="foot"><span class="flag"></span><p>This project has received funding from the Varnholt Assembly's Meridian 2020 research and innovation programme under grant agreement No 904417 Connected Services, Digital Trust &amp; Care Systems Resilience</p></footer>
</section>

<section class="slide col3 row1">
  <h2 class="head">SECTION TITLE HERE</h2>
  <div class="brand"><span class="dot"></span>KESTREL</div>
  <div class="member" style="left:16px"><div class="portrait" role="img" aria-label="Employee portrait"></div><h3>EMPLOYEE NAME</h3><h4>Company Name</h4><p class="copy center">Liquorice chupa chups applicake apple pie cupcake brownie bear claw cake gingerbread cotton candy. Bear claw croissant apple pie. Croissant cake sweet puff oreo . Liquorice chupa chups applicake apple pie cupcake brownie bear claw cake gingerbread cotton candy.</p></div>
  <div class="member" style="left:140px"><div class="portrait" role="img" aria-label="Employee portrait"></div><h3>EMPLOYEE NAME</h3><h4>Company Name</h4><p class="copy center">Liquorice chupa chups applicake apple pie cupcake brownie bear claw cake gingerbread cotton candy. Bear claw croissant apple pie. Croissant cake sweet puff oreo . Liquorice chupa chups applicake apple pie cupcake brownie bear claw cake gingerbread cotton candy.</p></div>
  <div class="member" style="left:264px"><div class="portrait" role="img" aria-label="Employee portrait"></div><h3>EMPLOYEE NAME</h3><h4>Company Name</h4><p class="copy center">Liquorice chupa chups applicake apple pie cupcake brownie bear claw cake gingerbread cotton candy. Bear claw croissant apple pie. Croissant cake sweet puff oreo . Liquorice chupa chups applicake apple pie cupcake brownie bear claw cake gingerbread cotton candy.</p></div>
  <footer class="foot"><span class="flag"></span><p>This project has received funding from the Varnholt Assembly's Meridian 2020 research and innovation programme under grant agreement No 904417 Connected Services, Digital Trust &amp; Care Systems Resilience</p></footer>
</section>

<section class="slide col1 row2">
  <h2 class="head">SECTION TITLE HERE</h2>
  <div class="brand"><span class="dot"></span>KESTREL</div>
  <div class="features">
    <div class="feature f1">
      <svg width="42" height="42" viewBox="0 0 42 42" fill="none" stroke="#fff" stroke-width="1.8"><circle cx="21" cy="21" r="19"/><ellipse cx="21" cy="21" rx="8" ry="19"/><line x1="2" y1="21" x2="40" y2="21"/><path d="M5 11h32M5 31h32"/></svg>
      <p class="copy center white">Liquorice chupa chups applicake apple pie cupcake brownie bear claw cake gingerbread cotton candy. Bear claw croissant apple pie. Croissant cake sweet puff oreo . Liquorice chupa chups applicake apple pie cupcake brownie bear claw cake gingerbread cotton candy. Bear claw croissant apple pie. Croissant cake sweet puff oreo.</p>
    </div>
    <div class="feature f2">
      <svg width="46" height="42" viewBox="0 0 46 42" fill="#fff"><circle cx="23" cy="5" r="3"/><circle cx="15" cy="9" r="3"/><circle cx="31" cy="9" r="3"/><circle cx="7" cy="15" r="3.5"/><circle cx="19" cy="15" r="3.5"/><circle cx="27" cy="15" r="3.5"/><circle cx="39" cy="15" r="3.5"/><rect x="3" y="20" width="8" height="20" rx="2"/><rect x="15" y="20" width="8" height="20" rx="2"/><rect x="23" y="20" width="8" height="20" rx="2"/><rect x="35" y="20" width="8" height="20" rx="2"/></svg>
      <p class="copy center white">Liquorice chupa chups applicake apple pie cupcake brownie bear claw cake gingerbread cotton candy. Bear claw croissant apple pie. Croissant cake sweet puff oreo . Liquorice chupa chups applicake apple pie cupcake brownie bear claw cake gingerbread cotton candy. Bear claw croissant apple pie. Croissant cake sweet puff oreo.</p>
    </div>
    <div class="feature f3">
      <svg width="46" height="42" viewBox="0 0 46 42" fill="none" stroke="#fff" stroke-width="1.6"><rect x="2" y="2" width="42" height="38"/><line x1="2" y1="9" x2="44" y2="9"/><circle cx="23" cy="17" r="3"/><path d="M21 21h4l1 12-3 4-3-4z"/></svg>
      <p class="copy center white">Liquorice chupa chups applicake apple pie cupcake brownie bear claw cake gingerbread cotton candy. Bear claw croissant apple pie. Croissant cake sweet puff oreo . Liquorice chupa chups applicake apple pie cupcake brownie bear claw cake gingerbread cotton candy. Bear claw croissant apple pie. Croissant cake sweet puff oreo.</p>
    </div>
    <div class="feature f4">
      <svg width="46" height="42" viewBox="0 0 46 42" fill="none" stroke="#fff" stroke-width="1.6"><circle cx="15" cy="14" r="12"/><circle cx="15" cy="11" r="3.5"/><path d="M9 21c2-5 10-5 12 0"/><circle cx="30" cy="28" r="13"/><rect x="24" y="27" width="4" height="8"/><rect x="29" y="23" width="4" height="12"/><rect x="34" y="20" width="4" height="15"/></svg>
      <p class="copy center white">Liquorice chupa chups applicake apple pie cupcake brownie bear claw cake gingerbread cotton candy. Bear claw croissant apple pie. Croissant cake sweet puff oreo . Liquorice chupa chups applicake apple pie cupcake brownie bear claw cake.</p>
    </div>
  </div>
  <footer class="foot"><span class="flag"></span><p>This project has received funding from the Varnholt Assembly's Meridian 2020 research and innovation programme under grant agreement No 904417 Connected Services, Digital Trust &amp; Care Systems Resilience</p></footer>
</section>

<section class="slide col2 row2">
  <h2 class="head">SECTION TITLE HERE</h2>
  <div class="brand"><span class="dot"></span>KESTREL</div>
  <div class="media" style="left:32px;top:52px;width:150px;height:88px" role="img" aria-label="Cloud network illustration"></div>
  <div class="media" style="left:222px;top:52px;width:150px;height:88px" role="img" aria-label="Cloud network illustration"></div>
  <div style="position:absolute;left:16px;top:147px;width:168px">
    <h3 class="ptitle"><span class="ring"></span>Paragraph title here</h3>
    <p class="copy" style="padding-left:17px">Liquorice chupa chups applicake apple pie cupcake brownie bear claw cake gingerbread cotton candy. Bear claw croissant apple pie. Croissant cake sweet puff oreo . Liquorice chupa chups applicake apple pie cupcake brownie bear claw . Liquorice chupa chups applicake apple pie cupcake brownie bear claw cake gingerbread cotton candy. Bear claw croissant apple pie. Croissant cake sweet puff oreo .</p>
  </div>
  <div style="position:absolute;left:206px;top:147px;width:168px">
    <h3 class="ptitle"><span class="ring"></span>Paragraph title here</h3>
    <p class="copy" style="padding-left:17px">Liquorice chupa chups applicake apple pie cupcake brownie bear claw cake gingerbread cotton candy. Bear claw croissant apple pie. Croissant cake sweet puff oreo . Liquorice chupa chups applicake apple pie cupcake brownie bear claw . Liquorice chupa chups applicake apple pie cupcake brownie bear claw cake gingerbread cotton candy. Bear claw croissant apple pie. Croissant cake sweet puff oreo .</p>
  </div>
  <footer class="foot"><span class="flag"></span><p>This project has received funding from the Varnholt Assembly's Meridian 2020 research and innovation programme under grant agreement No 904417 Connected Services, Digital Trust &amp; Care Systems Resilience</p></footer>
</section>

<section class="slide col3 row2">
  <h2 class="head">SECTION TITLE HERE</h2>
  <div class="brand"><span class="dot"></span>KESTREL</div>
  <div style="position:absolute;left:10px;top:51px;width:172px">
    <h3 class="ptitle"><span class="ring"></span>Paragraph title here</h3>
    <p class="copy" style="padding-left:8px">Liquorice chupa chups applicake apple pie cupcake brownie bear claw cake gingerbread cotton candy. Bear claw croissant apple pie. Croissant cake sweet puff oreo . Liquorice chupa chups applicake apple pie cupcake brownie bear claw . Liquorice chupa chups applicake apple pie cupcake brownie bear claw cake gingerbread cotton candy. Bear claw croissant apple pie. Croissant cake sweet puff oreo . Liquorice chupa chups applicake apple pie cupcake brownie bear claw . Liquorice chupa chups applicake apple pie cupcake brownie bear claw cake gingerbread cotton candy. Bear claw croissant apple pie. Croissant cake sweet puff oreo . Liquorice chupa chups applicake apple pie cupcake brownie bear claw . Liquorice chupa chups applicake apple pie cupcake brownie bear claw cake gingerbread cotton candy. Bear claw croissant apple pie. Croissant cake sweet puff oreo .</p>
  </div>
  <div class="media" style="left:195px;top:60px;width:191px;height:145px" role="img" aria-label="Cloud security network illustration"></div>
  <footer class="foot"><span class="flag"></span><p>This project has received funding from the Varnholt Assembly's Meridian 2020 research and innovation programme under grant agreement No 904417 Connected Services, Digital Trust &amp; Care Systems Resilience</p></footer>
</section>

<section class="slide col1 row3">
  <h2 class="head">SECTION TITLE HERE</h2>
  <div class="brand"><span class="dot"></span>KESTREL</div>
  <div class="band" style="top:27px;height:226px"></div>
  <div class="media thumb" style="left:15px;background:linear-gradient(135deg,#0d4f9a,#2a8fd6)" role="img" aria-label="Digital security grid image"></div>
  <div class="media thumb" style="left:142px;background:linear-gradient(135deg,#0d4f9a,#2a8fd6)" role="img" aria-label="Digital security grid image"></div>
  <div class="media thumb" style="left:269px;background:linear-gradient(135deg,#0d4f9a,#2a8fd6)" role="img" aria-label="Digital security grid image"></div>
  <div class="thumb-text" style="left:15px"><h3>Image title here</h3><p class="copy white">Liquorice chupa chups applicake apple pie cupcake brownie bear claw cake gingerbread cotton candy. Bear claw croissant apple pie. Croissant cake sweet puff oreo . Liquorice chupa chups applicake apple pie cupcake brownie bear claw . Liquorice chupa chups applicake apple pie cupcake brownie bear claw cake gingerbread cotton candy. Bear claw croissant apple pie.</p></div>
  <div class="thumb-text" style="left:142px"><h3>Image title here</h3><p class="copy white">Liquorice chupa chups applicake apple pie cupcake brownie bear claw cake gingerbread cotton candy. Bear claw croissant apple pie. Croissant cake sweet puff oreo . Liquorice chupa chups applicake apple pie cupcake brownie bear claw . Liquorice chupa chups applicake apple pie cupcake brownie bear claw cake gingerbread cotton candy. Bear claw croissant apple pie.</p></div>
  <div class="thumb-text" style="left:269px"><h3>Image title here</h3><p class="copy white">Liquorice chupa chups applicake apple pie cupcake brownie bear claw cake gingerbread cotton candy. Bear claw croissant apple pie. Croissant cake sweet puff oreo . Liquorice chupa chups applicake apple pie cupcake brownie bear claw . Liquorice chupa chups applicake apple pie cupcake brownie bear claw cake gingerbread cotton candy. Bear claw croissant apple pie.</p></div>
  <footer class="foot"><span class="flag"></span><p>This project has received funding from the Varnholt Assembly's Meridian 2020 research and innovation programme under grant agreement No 904417 Connected Services, Digital Trust &amp; Care Systems Resilience</p></footer>
</section>

<section class="slide col2 row3">
  <h2 class="head">SECTION TITLE HERE</h2>
  <div class="brand"><span class="dot"></span>KESTREL</div>
  <div class="band" style="top:27px;height:226px"></div>
  <div class="media" style="left:0;top:27px;width:155px;height:226px;background:linear-gradient(160deg,#c9ece8,#3fb7ad 50%,#0f6d68)" role="img" aria-label="Office building photograph"></div>
  <div class="label">INFRASTRUCTURE</div>
  <div style="position:absolute;left:196px;top:48px;width:180px">
    <p class="copy white">Liquorice chupa chups applicake apple pie cupcake brownie bear claw cake gingerbread cotton candy. Bear claw croissant apple pie. Croissant cake sweet puff oreo . Liquorice chupa chups applicake apple pie cupcake brownie bear claw cake gingerbread cotton candy. Bear claw croissant apple pie.</p>
    <p class="copy white" style="margin-top:8px">Croissant cake sweet puff oreo . Liquorice chupa chups applicake apple pie cupcake brownie bear claw . Liquorice chupa chups applicake apple pie cupcake brownie bear claw cake gingerbread cotton candy. Bear claw croissant apple pie. Croissant cake sweet puff oreo . Liquorice chupa chups applicake apple pie cupcake brownie bear claw cake gingerbread cotton candy. Bear claw croissant apple pie. Croissant cake sweet puff oreo .</p>
    <p class="copy white" style="margin-top:8px">Liquorice chupa chups applicake apple pie cupcake brownie bear claw. Liquorice chupa chups applicake apple pie cupcake brownie bear claw . Liquorice chupa chups applicake apple pie cupcake brownie bear claw .</p>
  </div>
  <footer class="foot"><span class="flag"></span><p>This project has received funding from the Varnholt Assembly's Meridian 2020 research and innovation programme under grant agreement No 904417 Connected Services, Digital Trust &amp; Care Systems Resilience</p></footer>
</section>

<section class="slide col3 row3">
  <h2 class="head">SECTION TITLE HERE</h2>
  <div class="brand"><span class="dot"></span>KESTREL</div>
  <div class="media" style="left:0;top:27px;width:386px;height:123px;background:linear-gradient(#d6d6d6,#6d6d6d)" role="img" aria-label="Group photograph of the kickoff meeting team"></div>
  <div class="band" style="top:150px;height:103px;padding:10px 11px 0">
    <h3 class="kick-title">OUT KICKOFF MEETING</h3>
    <p class="copy white">Liquorice chupa chups applicake apple pie cupcake brownie bear claw cake gingerbread cotton candy. Bear claw croissant apple pie. Croissant cake sweet puff oreo . Liquorice chupa chups applicake apple pie cupcake brownie bear claw . Liquorice chupa chups applicake apple pie cupcake brownie bear claw cake gingerbread cotton candy. Bear claw croissant apple pie. Croissant cake sweet puff oreo . Liquorice chupa chups applicake apple pie cupcake brownie bear claw cake gingerbread cotton candy. Bear claw croissant apple pie. Croissant cake sweet puff oreo . Liquorice chupa chups applicake apple pie cupcake brownie bear claw cake gingerbread cotton candy. Bear claw croissant apple pie. Croissant cake sweet puff oreo .</p>
  </div>
  <footer class="foot"><span class="flag"></span><p>This project has received funding from the Varnholt Assembly's Meridian 2020 research and innovation programme under grant agreement No 904417 Connected Services, Digital Trust &amp; Care Systems Resilience</p></footer>
</section>

<section class="slide col1 row4">
  <h2 class="head">SECTION TITLE HERE</h2>
  <div class="brand"><span class="dot"></span>KESTREL</div>
  <div class="bullet" style="top:52px"><h3 class="ptitle"><span class="ring"></span>Bullet title text here</h3><p class="copy" style="padding-left:13px">Liquorice chupa chups applicake apple pie cupcake brownie bear claw cake gingerbread cotton candy. Bear claw croissant apple pie. Croissant cake sweet puff oreo . Liquorice chupa chups applicake apple pie cupcake brownie bear claw . Liquorice chupa chups applicake apple pie cupcake brownie bear claw cake gingerbread cotton candy. Bear claw croissant apple pie. Croissant cake sweet puff oreo . Liquorice chupa chups applicake apple pie cupcake brownie bear claw .</p></div>
  <div class="bullet" style="top:114px"><h3 class="ptitle"><span class="ring"></span>Bullet title text here</h3><p class="copy" style="padding-left:13px">Liquorice chupa chups applicake apple pie cupcake brownie bear claw cake gingerbread cotton candy. Bear claw croissant apple pie. Croissant cake sweet puff oreo . Liquorice chupa chups applicake apple pie cupcake brownie bear claw . Liquorice chupa chups applicake apple pie cupcake brownie bear claw cake gingerbread cotton candy. Bear claw croissant apple pie. Croissant cake sweet puff oreo . Liquorice chupa chups applicake apple pie cupcake brownie bear claw .</p></div>
  <div class="bullet" style="top:176px"><h3 class="ptitle"><span class="ring"></span>Bullet title text here</h3><p class="copy" style="padding-left:13px">Liquorice chupa chups applicake apple pie cupcake brownie bear claw cake gingerbread cotton candy. Bear claw croissant apple pie. Croissant cake sweet puff oreo . Liquorice chupa chups applicake apple pie cupcake brownie bear claw . Liquorice chupa chups applicake apple pie cupcake brownie bear claw cake gingerbread cotton candy. Bear claw croissant apple pie. Croissant cake sweet puff oreo . Liquorice chupa chups applicake apple pie cupcake brownie bear claw .</p></div>
  <footer class="foot"><span class="flag"></span><p>This project has received funding from the Varnholt Assembly's Meridian 2020 research and innovation programme under grant agreement No 904417 Connected Services, Digital Trust &amp; Care Systems Resilience</p></footer>
</section>

<section class="slide col2 row4">
  <h2 class="head">SECTION TITLE HERE</h2>
  <div class="brand"><span class="dot"></span>KESTREL</div>
  <div style="position:absolute;left:10px;top:52px;width:176px">
    <h3 class="ptitle"><span class="ring"></span>Paragraph title here</h3>
    <p class="copy" style="padding-left:17px">Liquorice chupa chups applicake apple pie cupcake brownie bear claw cake gingerbread cotton candy. Bear claw croissant apple pie. Croissant cake sweet puff oreo . Liquorice chupa chups applicake apple pie cupcake brownie bear claw . Liquorice chupa chups applicake apple pie cupcake brownie bear claw cake gingerbread cotton candy. Bear claw croissant apple pie. Croissant cake sweet puff oreo . Liquorice chupa chups applicake apple pie cupcake brownie bear claw . Liquorice chupa chups applicake apple pie cupcake brownie bear claw cake gingerbread cotton candy. Bear claw croissant apple pie. Croissant cake sweet puff oreo . Liquorice chupa chups applicake apple pie cupcake brownie bear claw . Liquorice chupa chups applicake apple pie cupcake brownie bear claw cake gingerbread cotton candy. Bear claw croissant apple pie. Croissant cake sweet puff oreo .</p>
  </div>
  <div style="position:absolute;left:200px;top:52px;width:176px">
    <h3 class="ptitle"><span class="ring"></span>Paragraph title here</h3>
    <p class="copy" style="padding-left:17px">Liquorice chupa chups applicake apple pie cupcake brownie bear claw cake gingerbread cotton candy. Bear claw croissant apple pie. Croissant cake sweet puff oreo . Liquorice chupa chups applicake apple pie cupcake brownie bear claw . Liquorice chupa chups applicake apple pie cupcake brownie bear claw cake gingerbread cotton candy. Bear claw croissant apple pie. Croissant cake sweet puff oreo . Liquorice chupa chups applicake apple pie cupcake brownie bear claw . Liquorice chupa chups applicake apple pie cupcake brownie bear claw cake gingerbread cotton candy. Bear claw croissant apple pie. Croissant cake sweet puff oreo . Liquorice chupa chups applicake apple pie cupcake brownie bear claw . Liquorice chupa chups applicake apple pie cupcake brownie bear claw cake gingerbread cotton candy. Bear claw croissant apple pie. Croissant cake sweet puff oreo .</p>
  </div>
  <footer class="foot"><span class="flag"></span><p>This project has received funding from the Varnholt Assembly's Meridian 2020 research and innovation programme under grant agreement No 904417 Connected Services, Digital Trust &amp; Care Systems Resilience</p></footer>
</section>

<section class="slide col3 row4">
  <h2 class="head">SECTION TITLE HERE</h2>
  <div class="brand"><span class="dot"></span>KESTREL</div>
  <p class="copy" style="position:absolute;left:16px;top:38px;width:360px">Liquorice chupa chups applicake apple pie cupcake brownie bear claw cake gingerbread cotton candy. Bear claw croissant apple pie. Croissant cake sweet puff oreo . Liquorice chupa chups applicake apple pie cupcake brownie bear claw Liquorice chupa chups applicake apple pie cupcake brownie bear claw cake gingerbread cotton candy. Bear claw croissant apple pie. Croissant cake sweet puff oreo . Liquorice chupa chups applicake apple pie cupcake brownie bear claw . Liquorice chupa chups applicake apple pie cupcake brownie bear claw cake gingerbread cotton candy. Bear claw croissant apple pie. Croissant cake sweet puff oreo .</p>
  <table class="grid">
    <thead><tr><th style="text-align:center">SECTION</th><th>MAIN TITLE HERE</th></tr></thead>
    <tbody>
      <tr><td class="key">ICON - 1</td><td>Liquorice chupa chups applicake apple pie cupcake brownie bear claw cake gingerbread cotton candy. Bear claw croissant apple pie. Croissant cake sweet puff oreo . Liquorice chupa chups applicake apple pie</td></tr>
      <tr><td class="key">ICON - 1</td><td>Liquorice chupa chups applicake apple pie cupcake brownie bear claw cake gingerbread cotton candy. Bear claw croissant apple pie. Croissant cake sweet puff oreo . Liquorice chupa chups applicake apple pie</td></tr>
      <tr><td class="key">ICON - 1</td><td>Liquorice chupa chups applicake apple pie cupcake brownie bear claw cake gingerbread cotton candy. Bear claw croissant apple pie. Croissant cake sweet puff oreo . Liquorice chupa chups applicake apple pie</td></tr>
      <tr><td class="key">ICON - 1</td><td>Liquorice chupa chups applicake apple pie cupcake brownie bear claw cake gingerbread cotton candy. Bear claw croissant apple pie. Croissant cake sweet puff oreo . Liquorice chupa chups applicake apple pie</td></tr>
      <tr><td class="key">ICON - 1</td><td>Liquorice chupa chups applicake apple pie cupcake brownie bear claw cake gingerbread cotton candy. Bear claw croissant apple pie. Croissant cake sweet puff oreo . Liquorice chupa chups applicake apple pie</td></tr>
    </tbody>
  </table>
  <footer class="foot"><span class="flag"></span><p>This project has received funding from the Varnholt Assembly's Meridian 2020 research and innovation programme under grant agreement No 904417 Connected Services, Digital Trust &amp; Care Systems Resilience</p></footer>
</section>

</body>
</html>
```